Stonefield Crew Brochure = SCB $$$

this brochure will be used for a canvassing campaign (door to door) appointment setting

the campaign will be for homeowners that would like to do any kind of improvement to their house - home improvement
from EXT paint or roof repair all the way to kitchen and bathroom remodeling

we want to catch the prospect eye with the brochure and to educate our prospect about the different ways they could improve their house step by step to their dream house

Target Market(s)

Homeowners
anyone who would like to improve or fix any part of their house

Industry/Entity Type

Home Improvement

Contact Information for Business Card

the green roof house blueprints on one side
the Stonefield Crew logo on the other side

Font styles to use
Serif
Decorative

Colors
ffffff
886aae
9bcb3b
e6e6e6

Requirements
Must have
• this is a TRI-FOLD brochure
• call for action -- schedule your free estimate
• or any idea that will lead to set up an appointment with our specialist
• LOOK AT MY WEBSITE TO UNDERSTAND MORE WHAT I LIKE
• WWW.THESTONEFIELDCREWS-EXAMPLE.COM
• services:
• Kitchen Renovations
• Bathroom Renovations
• Modern Landscaping
• Additions + in-law quarters
• Exterior paint +interior paint
• wood replacement + stucco repair
• roof repair
• railling and glass work
Nice to have
• the pictures I have uploaded can use as an example but im open to other ideas...
• THERE IS NO SUBSTITUTE FOR QUALITY.
• the picture of the women in the kitchen--
• i enjoy making food and spending time in my new kitchen, to see my whole family sitting down to eat dinner together in our perfect little kitchen make me so happy
Should not have
• the 2 brochures i have uploaded are for example only

```html
<!DOCTYPE html>
<html lang="en">
<head>
<meta charset="utf-8">
<title>Stonefield Crew Brochure</title>
<link href="https://fonts.googleapis.com/css2?family=Montserrat:wght@400;600;700;800&family=Open+Sans:wght@400;600;700&display=swap" rel="stylesheet">
<style>
  :root {
    --backdrop: #e6e6e6;
    --white: #ffffff;
    --paper: #f4f4f4;
    --green: #6cb33f;
    --green-light: #9bcb3b;
    --green-dark: #3f7d22;
    --purple: #886aae;
    --ink: #2b2b2b;
    --photo-wood: #8a5a34;
    --photo-wood-dark: #4e2f1a;
    --photo-kitchen: #b98a5e;
    --photo-kitchen-light: #d9d4cc;
  }
  * { margin: 0; padding: 0; box-sizing: border-box; }
  html, body { width: 1200px; height: 800px; overflow: hidden; background: var(--backdrop); }
  .brochure {
    position: absolute; left: 45px; top: 40px; width: 1110px; height: 720px;
    box-shadow: 0 8px 24px rgba(0,0,0,.18);
    font-family: "Open Sans", sans-serif; color: var(--white);
  }
  .brochure-shapes { position: absolute; inset: 0; }
  .fold { stroke: rgba(0,0,0,.12); stroke-width: 1; }

  .tagline {
    position: absolute; left: 40px; top: 540px;
    font-family: "Montserrat", sans-serif; font-weight: 400; font-size: 17px; line-height: 1.1;
    color: rgba(255,255,255,.85);
  }
  .motto {
    position: absolute; left: 40px; top: 600px;
    font-family: "Montserrat", sans-serif; font-weight: 800; font-size: 34px; line-height: 1.02;
    letter-spacing: .5px;
  }
  .badge-text {
    position: absolute; left: 232px; top: 480px; width: 110px; text-align: center;
    font-family: "Montserrat", sans-serif; font-weight: 700; font-size: 11px; line-height: 1.25;
    color: var(--ink);
  }

  .services-title {
    position: absolute; left: 470px; top: 262px; width: 250px; text-align: right;
    font-family: "Montserrat", sans-serif; font-weight: 700; font-size: 17px; line-height: 1.1;
  }
  .services { position: absolute; left: 400px; top: 352px; width: 315px; list-style: none; }
  .service { margin-bottom: 10px; }
  .service-name { font-weight: 700; font-size: 12px; margin-bottom: 2px; }
  .service-text { font-size: 9.5px; line-height: 1.4; color: rgba(255,255,255,.92); }
  .more-title {
    position: absolute; left: 400px; top: 600px;
    font-weight: 700; font-size: 12px;
  }
  .more-services {
    position: absolute; left: 400px; top: 620px; width: 315px; list-style: none;
    display: grid; grid-template-columns: 1fr 1fr; column-gap: 12px; row-gap: 4px;
    font-size: 9.5px; line-height: 1.3;
  }
  .more-services li { position: relative; padding-left: 12px; }
  .more-services li::before {
    content: ""; position: absolute; left: 0; top: 4px; width: 6px; height: 6px;
    border-radius: 50%; background: var(--purple);
  }
  .quality {
    position: absolute; left: 400px; top: 682px; width: 315px;
    font-family: "Montserrat", sans-serif; font-weight: 700; font-size: 11px; letter-spacing: .5px;
  }

  .call-head {
    position: absolute; left: 780px; top: 28px;
    font-family: "Montserrat", sans-serif; font-weight: 600; font-size: 19px; line-height: 1.15;
    color: var(--green);
  }
  .call-phone {
    position: absolute; left: 780px; top: 76px;
    font-family: "Montserrat", sans-serif; font-weight: 600; font-size: 32px; color: var(--ink);
  }
  .call-note {
    position: absolute; left: 780px; top: 122px; width: 280px;
    font-size: 10.5px; font-weight: 600; line-height: 1.35; color: var(--ink);
  }
  .cta {
    position: absolute; left: 780px; top: 162px; padding: 8px 16px;
    background: var(--purple); border-radius: 3px;
    font-family: "Montserrat", sans-serif; font-weight: 700; font-size: 12px; letter-spacing: .5px;
    color: var(--white); text-transform: uppercase;
  }
  .brand {
    position: absolute; right: 30px; bottom: 52px; display: flex; align-items: center; gap: 10px;
  }
  .brand-dot { width: 34px; height: 34px; border-radius: 50%; background: var(--green-dark); }
  .brand-name {
    font-family: "Montserrat", sans-serif; font-weight: 600; font-size: 20px; color: var(--white);
    letter-spacing: 1px; text-transform: uppercase;
  }
  .website {
    position: absolute; right: 30px; bottom: 24px;
    font-family: "Montserrat", sans-serif; font-weight: 600; font-size: 10.5px; letter-spacing: .5px;
    color: var(--white);
  }
</style>
</head>
<body>
<main class="brochure">
  <svg class="brochure-shapes" width="1110" height="720" viewBox="0 0 1110 720">
    <defs>
      <linearGradient id="wood" x1="0" y1="0" x2="1" y2="1">
        <stop offset="0" stop-color="#8a5a34"/>
        <stop offset="1" stop-color="#4e2f1a"/>
      </linearGradient>
      <linearGradient id="kitchen" x1="0" y1="0" x2="0" y2="1">
        <stop offset="0" stop-color="#d9d4cc"/>
        <stop offset="1" stop-color="#b98a5e"/>
      </linearGradient>
      <linearGradient id="leaf" x1="0" y1="0" x2="0" y2="1">
        <stop offset="0" stop-color="#6cb33f"/>
        <stop offset="1" stop-color="#9bcb3b"/>
      </linearGradient>
    </defs>

    <rect x="0" y="0" width="740" height="720" fill="url(#wood)" role="img"
      aria-label="Photo: a couple and a builder reviewing plans by the windows of a framed-out room"/>
    <path d="M0,500 Q180,440 370,470 L370,720 L0,720 Z" fill="url(#leaf)"/>
    <path d="M200,470 Q290,455 370,470 L370,520 Q300,480 200,470 Z" fill="#3f7d22" opacity=".5"/>
    <path d="M370,310 Q540,220 740,180 L740,720 L370,720 Z" fill="#6cb33f"/>
    <path d="M370,310 Q540,220 740,180 L740,210 Q540,250 370,340 Z" fill="#9bcb3b"/>

    <rect x="740" y="0" width="370" height="720" fill="#f4f4f4"/>
    <path d="M740,360 Q900,250 1110,205 L1110,720 L740,720 Z" fill="#6cb33f"/>
    <path d="M740,385 Q900,275 1110,230 L1110,720 L740,720 Z" fill="#886aae"/>
    <path d="M740,405 Q900,295 1110,250 L1110,720 L740,720 Z" fill="url(#kitchen)" role="img"
      aria-label="Photo: bright kitchen with grey cabinets, wooden island and stool, and oak floor"/>

    <polygon points="287,440 342,468 342,528 287,556 232,528 232,468" fill="#ffffff"/>
    <circle cx="287" cy="464" r="11" fill="none" stroke="#3f7d22" stroke-width="2.5"/>
    <path d="M281,464 L286,469 L294,459" fill="none" stroke="#3f7d22" stroke-width="2.5" stroke-linecap="round"/>

    <line class="fold" x1="370" y1="0" x2="370" y2="720"/>
    <line class="fold" x1="740" y1="0" x2="740" y2="720"/>
  </svg>

  <section class="panel-cover">
    <p class="badge-text">INNOVATIVE,<br>FULL SERVICE<br>DESIGN/BUILD</p>
    <p class="tagline">Building a<br>better world<br>one day at a time.</p>
    <h1 class="motto">WE DESIGN<br>WE BUILD<br>WE CREATE</h1>
  </section>

  <section class="panel-services">
    <h2 class="services-title">BUILD THE LIFE<br>OF YOUR DREAMS</h2>
    <ul class="services">
      <li class="service">
        <h3 class="service-name">Kitchen Renovations</h3>
        <p class="service-text">The Kitchen is the heart of the home, where the family gathers for dinner. Shouldn't yours invite everyone in?</p>
      </li>
      <li class="service">
        <h3 class="service-name">Bathroom Renovations</h3>
        <p class="service-text">Relax after a long day in a Bathroom that feels like a high-end spa, right in your own home.</p>
      </li>
      <li class="service">
        <h3 class="service-name">Modern Landscaping</h3>
        <p class="service-text">Be the neighbor with the lawn everyone stops to admire, with drought-tolerant gardens for a dry climate.</p>
      </li>
      <li class="service">
        <h3 class="service-name">Additions + In-Law Quarters</h3>
        <p class="service-text">More room for a growing family, built to blend in with the home you already love.</p>
      </li>
    </ul>
    <h3 class="more-title">Step by step, we also handle:</h3>
    <ul class="more-services">
      <li>Exterior + interior paint</li>
      <li>Roof repair</li>
      <li>Wood replacement</li>
      <li>Stucco repair</li>
      <li>Railing + glass work</li>
      <li>New construction</li>
    </ul>
    <p class="quality">THERE IS NO SUBSTITUTE FOR QUALITY.</p>
  </section>

  <section class="panel-contact">
    <h2 class="call-head">Living The Dream Is Just<br>One Phone Call Away.</h2>
    <p class="call-phone">(555) 014-2290</p>
    <p class="call-note">Don't waste any more time, start your project with Stonefield Crew, today!</p>
    <p class="cta">Schedule your free estimate</p>
    <div class="brand">
      <span class="brand-dot"></span>
      <span class="brand-name">Stonefield Crew</span>
    </div>
    <p class="website">WWW.THESTONEFIELDCREWS-EXAMPLE.COM</p>
  </section>
</main>
</body>
</html>
```